business cards for Tramvex
Tramvexa
business cards for Tramvex - Government
Modern
R.K.Dunmore
914 E Harlan Avenue, Suite 215 Fort Worth, TX 76102
rdunmore@tramvexa-mail.com
www.tramvexa-site.com
need to be able to create cards for other people- the backside is logo only- the front needs my name then tramvexa with address email phone number and website- please put logo on front side as well. colors can be red/white/blue/ black or any combination
big version of logo and possibly ability to write on it- this may not work out well so if it doesn't then don't do it.

```html
<!DOCTYPE html>
<html lang="en">
<head>
<meta charset="utf-8">
<title>Tramvexa – Business Card</title>
<link rel="stylesheet" href="https://fonts.googleapis.com/css2?family=Exo+2:wght@400;500&family=Cinzel:wght@500&display=swap">
<style>
  :root {
    --backdrop: #e9e9ec;
    --card: #ffffff;
    --navy: #1f2a55;
    --crimson: #b3282d;
    --ink: #2b2e38;
  }
  html, body {
    margin: 0;
    width: 1200px;
    height: 816px;
    overflow: hidden;
    background: var(--backdrop);
  }
  .canvas {
    position: relative;
    width: 1200px;
    height: 816px;
  }
  .card {
    position: absolute;
    left: 100px;
    top: 118px;
    width: 1000px;
    height: 580px;
    background: var(--card);
    border-radius: 44px;
    box-shadow: 0 10px 30px rgba(20, 24, 40, 0.12);
    font-family: "Exo 2", sans-serif;
    color: var(--ink);
  }
  .rule-top {
    position: absolute;
    left: 150px;
    top: 150px;
    width: 330px;
    height: 4px;
    background: var(--navy);
  }
  .identity {
    position: absolute;
    left: 70px;
    top: 170px;
    display: flex;
    align-items: center;
    gap: 20px;
  }
  .badge {
    width: 50px;
    height: 50px;
    border-radius: 50%;
    background: var(--crimson);
    display: flex;
    align-items: center;
    justify-content: center;
  }
  .person-name {
    font-size: 26px;
    letter-spacing: 1.5px;
    text-transform: uppercase;
    color: var(--navy);
    line-height: 1.1;
  }
  .person-role {
    font-size: 21px;
    letter-spacing: 1.5px;
    color: var(--ink);
  }
  .rule-bottom {
    position: absolute;
    left: 70px;
    top: 258px;
    width: 410px;
    height: 4px;
    background: var(--navy);
  }
  .contacts {
    position: absolute;
    left: 70px;
    top: 292px;
    margin: 0;
    padding: 0;
    list-style: none;
  }
  .contact-row {
    display: flex;
    align-items: center;
    gap: 22px;
    margin-bottom: 22px;
  }
  .icon {
    flex: none;
    width: 46px;
    height: 46px;
    border-radius: 50%;
    background: var(--navy);
    display: flex;
    align-items: center;
    justify-content: center;
  }
  .contact-text {
    font-size: 20px;
    letter-spacing: 1px;
    line-height: 1.35;
  }
  .brand {
    position: absolute;
    right: 80px;
    top: 290px;
    display: flex;
    align-items: center;
    gap: 16px;
  }
  .brand-mark {
    width: 22px;
    height: 22px;
    background: var(--navy);
  }
  .brand-name {
    font-family: "Cinzel", serif;
    font-weight: 500;
    font-size: 54px;
    color: var(--navy);
    letter-spacing: 1px;
  }
</style>
</head>
<body>
<main class="canvas">
  <section class="card" aria-label="Business card front">
    <div class="rule-top"></div>

    <div class="identity">
      <div class="badge">
        <svg width="26" height="26" viewBox="0 0 24 24" aria-hidden="true">
          <circle cx="12" cy="8" r="4.5" fill="#fff"/>
          <path d="M3.5 21c0-4.7 3.8-7.5 8.5-7.5s8.5 2.8 8.5 7.5z" fill="#fff"/>
        </svg>
      </div>
      <div>
        <div class="person-name">Owen Hartley</div>
        <div class="person-role">Managing Director</div>
      </div>
    </div>

    <div class="rule-bottom"></div>

    <ul class="contacts">
      <li class="contact-row">
        <span class="icon">
          <svg width="20" height="24" viewBox="0 0 20 24" aria-hidden="true">
            <rect x="4" y="2" width="12" height="20" rx="2" fill="none" stroke="#fff" stroke-width="2"/>
            <circle cx="10" cy="18" r="1.3" fill="#fff"/>
          </svg>
        </span>
        <span class="contact-text">012 555 0147<br>012 555 0147</span>
      </li>
      <li class="contact-row">
        <span class="icon">
          <svg width="24" height="22" viewBox="0 0 24 22" aria-hidden="true">
            <rect x="2" y="2" width="20" height="13" rx="1.5" fill="none" stroke="#fff" stroke-width="2"/>
            <path d="M8 20h8M12 15v5" stroke="#fff" stroke-width="2"/>
          </svg>
        </span>
        <span class="contact-text">ohartley@tramvexa-mail.com<br>www.tramvexa-site.com</span>
      </li>
      <li class="contact-row">
        <span class="icon">
          <svg width="20" height="24" viewBox="0 0 20 24" aria-hidden="true">
            <path d="M10 2a7 7 0 0 0-7 7c0 5.2 7 13 7 13s7-7.8 7-13a7 7 0 0 0-7-7z" fill="#fff"/>
            <circle cx="10" cy="9" r="2.6" fill="var(--navy)"/>
          </svg>
        </span>
        <span class="contact-text">417 9th Floor,Plaza<br>Linden Road KVR</span>
      </li>
    </ul>

    <div class="brand">
      <span class="brand-mark"></span>
      <span class="brand-name">Tramvexa</span>
    </div>
  </section>
</main>
</body>
</html>
```